Re-design my 1-page website to be BETTER!

Hi Guys,
I recently created a 1-page website for market testing purposes for a company I am starting. Problem is, the feedback i've had on the page is its a bit corporate and boring.
I would love you to design something that is fresher, more modern and will generate leads (via the sign up CTA's).
Here is the website as it is now: www.guidebridgehub.com.au.
If you need any info or have questions, just reach out.
Thanks,
Oliver

Target Market(s)

Entrepreneurs

Number of Pages Required

1 page

Font styles to use
Sans Serif

Colors
abd036
34a6d7
ffffff

Requirements
Must have
• Fresh, Modern, high-converting
• I expect 70% of traffic to be mobile so must be mobile optimised first.
Nice to have
• I've highlighted colours i like below, however, I am open to suggestions. I like colours that are gender neutral and show energy and vibrancy.
• I have used Proxima Nova for the fonts, as I find it easy to read however, I am open to suggestions. My main preference is that it displays well and is easily read

```html
<!DOCTYPE html>
<html lang="en">
<head>
<meta charset="utf-8">
<title>GuideBridge Hub – One Page Site</title>
<link href="https://fonts.googleapis.com/css2?family=Poppins:wght@300;400;500;600;700&display=swap" rel="stylesheet">
<style>
:root{
  --board:#1c3550;
  --green:#34a21f;
  --green-dark:#1f7a16;
  --blue:#2b7fcb;
  --teal:#1fa6b8;
  --ink:#222;
  --text:#444;
  --muted:#777;
  --grey-band:#eeeeee;
  --line:#d9d9d9;
  --white:#fff;
}
*{box-sizing:border-box;margin:0;padding:0}
html,body{width:1200px;height:3403px;overflow:hidden}
body{background:var(--board);font-family:"Poppins",sans-serif;color:var(--text);position:relative}
.screen{position:absolute;background:var(--white);overflow:hidden}
.desktop{left:97px;top:79px;width:751px;height:2738px}
.mobile{left:943px;top:75px;width:162px;height:3259px}
.band{position:absolute;left:0;width:100%;overflow:hidden;text-align:center}
.logo{font-weight:600;color:var(--green);letter-spacing:.5px}
.btn-solid{display:inline-block;background:var(--green);color:#fff;font-weight:600;letter-spacing:.6px}
.btn-line{display:inline-block;border:1.5px solid var(--green);color:var(--green);font-weight:600;letter-spacing:.6px;background:#fff}
.btn-light{display:inline-block;border:1.5px solid #fff;color:#fff;font-weight:600;letter-spacing:.6px}
.hero-photo{position:absolute;inset:0;background:linear-gradient(120deg,#8a7a6c 0%,#c9bfb3 35%,#6d6a66 60%,#a39b92 100%)}
.hero-shade{position:absolute;inset:0;background:rgba(20,20,20,.35)}
.cta-bg{position:absolute;inset:0;background:radial-gradient(ellipse at 30% 40%,#3fae2a 0%,#238a17 55%,#17650f 100%)}
.faq-bg{position:absolute;inset:0;background:linear-gradient(180deg,#f3f3f3,#e4e4e4 60%,#efefef)}
.card{color:#fff;text-align:center}
.card.blue{background:var(--blue)}
.card.green{background:var(--green)}
.card .ico{display:block;margin:0 auto;border:2px solid #fff;border-radius:50%}
.faq-item{display:flex;justify-content:space-between;align-items:center;background:#fff;border:1px solid var(--line);color:var(--text);text-align:left}
.faq-item .plus{background:var(--blue);color:#fff;display:flex;align-items:center;justify-content:center;font-weight:600}
.faq-open{background:var(--blue);color:#fff;text-align:left}
.social{display:inline-block;border-radius:50%;background:var(--blue)}
.feat-title{display:flex;align-items:center;font-weight:600;color:var(--ink);text-transform:uppercase;text-align:left}
.feat-title svg{flex:none}
.feat p{text-align:left}

/* ---------- desktop ---------- */
.d-nav{top:0;height:46px;display:flex;align-items:center;justify-content:space-between;padding:0 40px}
.d-nav .logo{font-size:14px}
.d-nav ul{display:flex;list-style:none;gap:14px;font-size:8.5px;font-weight:500;color:var(--ink)}
.d-hero{top:46px;height:378px;color:#fff}
.d-hero .inner{position:relative;padding-top:143px}
.d-hero .t1{font-size:23px;font-weight:300;letter-spacing:1px;line-height:1.1}
.d-hero .t2{font-size:24px;font-weight:600;letter-spacing:1px;line-height:1.3}
.d-hero .btn-solid{margin-top:12px;padding:8px 16px;font-size:10px}
.d-hero .mouse{display:block;margin:14px auto 0}
.d-find{top:424px;height:286px;padding:48px 145px 0}
.d-find h2{font-size:17px;font-weight:700;color:var(--ink);letter-spacing:.6px;margin-bottom:18px}
.d-find p{font-size:8.5px;line-height:1.65;margin-bottom:12px}
.d-find .btn-line{margin-top:6px;padding:7px 14px;font-size:8.5px}
.d-find small{display:block;margin-top:16px;font-size:7.5px;color:var(--muted)}
.d-mentor{top:710px;height:522px;background:var(--grey-band);padding:86px 0 0}
.d-mentor h2{font-size:22px;font-weight:600;color:var(--ink);margin-bottom:12px}
.d-mentor .sub{font-size:8.5px;line-height:2}
.d-cards{display:flex;justify-content:center;gap:22px;margin-top:30px}
.d-cards .card{width:177px;height:209px;padding:32px 14px 0}
.d-cards .ico{width:38px;height:38px}
.d-cards h3{font-size:10.5px;font-weight:600;margin:12px 0 6px}
.d-cards p{font-size:7.5px;line-height:1.55}
.d-mentor .btn-line{margin-top:40px;padding:7px 14px;font-size:8.5px}
.d-mentor small{display:block;margin-top:13px;font-size:7.5px;color:var(--muted)}
.d-how{top:1232px;height:605px;padding:52px 0 0}
.d-how h2{font-size:20px;font-weight:400;color:var(--ink);letter-spacing:1.2px;line-height:1.35}
.d-how h2 b{font-weight:700}
.d-feats{display:grid;grid-template-columns:repeat(3,180px);column-gap:20px;row-gap:20px;margin:40px 0 0 88px}
.d-feats .feat-title{font-size:10px;gap:8px;line-height:1.15;margin-bottom:8px}
.d-feats p{font-size:7.7px;line-height:1.6}
.d-how .btn-line{margin-top:34px;padding:7px 14px;font-size:8.5px}
.d-how small{display:block;margin-top:12px;font-size:7.5px;color:var(--muted)}
.d-faq{top:1837px;height:470px}
.d-faq .inner{position:relative;padding-top:40px}
.d-faq h2{font-size:22px;font-weight:500;color:var(--ink);margin-bottom:20px}
.d-faq .list{width:461px;margin:0 auto}
.d-faq .faq-item{height:22px;font-size:8px;padding-left:10px;margin-bottom:11px}
.d-faq .plus{width:16px;height:16px;margin-right:3px;border-radius:50%;font-size:11px}
.d-faq .faq-open{padding:10px 12px;font-size:8px;line-height:1.6;margin:-4px 0 12px;height:66px}
.d-cta{top:2307px;height:272px;color:#fff}
.d-cta .inner{position:relative;padding:48px 150px 0}
.d-cta h2{font-size:16px;font-weight:700;letter-spacing:1px;margin-bottom:10px}
.d-cta p{font-size:8.5px;line-height:1.6}
.d-cta .hl{font-size:12px;font-weight:500;margin:14px 0 14px}
.d-cta .btn-light{padding:7px 20px;font-size:8.5px}
.d-cta small{display:block;margin-top:16px;font-size:8px}
.d-foot{top:2579px;height:159px;padding-top:44px}
.d-foot .links{font-size:8px;color:var(--ink)}
.d-foot .copy{font-size:9px;color:var(--ink);margin-top:14px}
.d-foot .socials{margin-top:16px;display:flex;justify-content:center;gap:4px}
.d-foot .social{width:15px;height:15px}
.d-foot .top{position:absolute;right:32px;top:50px;font-size:9px;color:var(--muted)}

/* ---------- mobile ---------- */
.m-nav{top:0;height:23px;display:flex;align-items:center;justify-content:space-between;padding:0 6px}
.m-nav .logo{font-size:6.5px}
.m-nav .burger{width:8px;height:6px;border-top:1.2px solid #333;border-bottom:1.2px solid #333;position:relative}
.m-nav .burger::after{content:"";position:absolute;left:0;right:0;top:1.2px;border-top:1.2px solid #333}
.m-hero{top:23px;height:156px;color:#fff}
.m-hero .inner{position:relative;padding-top:52px}
.m-hero .t1{font-size:9px;font-weight:300}
.m-hero .t2{font-size:9px;font-weight:600}
.m-hero .btn-solid{margin-top:5px;padding:3px 7px;font-size:4.5px}
.m-find{top:179px;height:386px;padding:28px 12px 0}
.m-find h2{font-size:9.5px;font-weight:600;color:var(--ink);line-height:1.45;margin-bottom:10px}
.m-find p{font-size:5.6px;line-height:1.75;margin-bottom:7px}
.m-find .btn-line{margin-top:10px;padding:3px 7px;font-size:4.6px}
.m-find small{display:block;margin-top:15px;font-size:4.2px;color:var(--muted)}
.m-mentor{top:565px;height:846px;background:var(--grey-band);padding:28px 10px 0}
.m-mentor h2{font-size:11px;font-weight:600;color:var(--ink);line-height:1.45;margin-bottom:8px}
.m-mentor .sub{font-size:5.6px;line-height:1.75}
.m-cards .card{width:142px;height:181px;margin:16px auto 0;padding:24px 10px 0}
.m-cards .ico{width:30px;height:30px}
.m-cards h3{font-size:7px;font-weight:600;margin:10px 0 5px}
.m-cards p{font-size:5.2px;line-height:1.65}
.m-mentor .btn-line{margin-top:30px;padding:3px 7px;font-size:4.6px}
.m-mentor small{display:block;margin-top:9px;font-size:4.2px;color:var(--muted)}
.m-how{top:1411px;height:1020px;padding:26px 12px 0}
.m-how h2{font-size:10px;font-weight:400;color:var(--ink);letter-spacing:.5px;line-height:1.55}
.m-how h2 b{font-weight:700}
.m-feats{margin-top:20px}
.m-feats .feat{margin-bottom:12px}
.m-feats .feat-title{font-size:6.2px;gap:6px;line-height:1.2;margin-bottom:5px}
.m-feats p{font-size:5.2px;line-height:1.7}
.m-how .btn-line{margin-top:6px;padding:3px 7px;font-size:4.6px}
.m-how small{display:block;margin-top:8px;font-size:5.2px;line-height:1.6;color:var(--text)}
.m-faq{top:2431px;height:336px}
.m-faq .inner{position:relative;padding:28px 10px 0}
.m-faq h2{font-size:8.5px;font-weight:600;color:var(--ink);line-height:1.4;margin-bottom:10px}
.m-faq .faq-item{height:11px;font-size:4px;padding-left:4px;margin-bottom:6px}
.m-faq .plus{width:11px;height:11px;font-size:6px}
.m-faq .faq-open{padding:6px 5px;font-size:4px;line-height:1.6;margin-bottom:6px;height:44px}
.m-cta{top:2767px;height:292px;color:#fff}
.m-cta .inner{position:relative;padding:30px 10px 0}
.m-cta h2{font-size:11px;font-weight:700;line-height:1.35;margin-bottom:8px}
.m-cta p{font-size:5.4px;line-height:1.75}
.m-cta .hl{font-size:6.8px;font-weight:600;line-height:1.6;margin:8px 0}
.m-cta .btn-light{padding:4px 10px;font-size:4.8px}
.m-cta small{display:block;margin-top:12px;font-size:5.4px;line-height:1.7}
.m-foot{top:3059px;height:200px;padding:40px 10px 0;text-align:left}
.m-foot .links{font-size:5.2px;line-height:2.1;color:var(--ink)}
.m-foot .copy{font-size:5.6px;line-height:1.8;color:var(--ink);margin-top:8px}
.m-foot .socials{margin-top:10px;display:flex;gap:3px;align-items:center}
.m-foot .social{width:8px;height:8px}
.m-foot .top{margin-left:auto;font-size:6px;color:var(--muted)}
</style>
</head>
<body>

<!-- ===================== DESKTOP ===================== -->
<main class="screen desktop">
  <header class="band d-nav">
    <span class="logo">GUIDEBRIDGE HUB</span>
    <ul><li>HOME</li><li>MENTORSHIP</li><li>FIND MY MENTOR</li><li>FAQS</li><li>ABOUT</li><li>CONTACT</li></ul>
  </header>

  <section class="band d-hero">
    <div class="hero-photo" role="img" aria-label="Photo of a mentor and two entrepreneurs in conversation at a bright office desk"></div>
    <div class="hero-shade"></div>
    <div class="inner">
      <div class="t1">GUIDEBRIDGE HUB</div>
      <div class="t2">A MENTOR FOR EVERYONE</div>
      <span class="btn-solid">FIND MY MENTOR</span>
      <svg class="mouse" width="16" height="40" viewBox="0 0 16 40"><rect x="2" y="1" width="12" height="19" rx="6" fill="none" stroke="#fff" stroke-width="1.5"/><line x1="8" y1="5" x2="8" y2="9" stroke="#fff" stroke-width="1.5"/><path d="M4 25l4 4 4-4M4 31l4 4 4-4" fill="none" stroke="#fff" stroke-width="1.3"/></svg>
    </div>
  </section>

  <section class="band d-find">
    <h2>FINDING A MENTOR HAS NEVER BEEN EASIER</h2>
    <p>Having a great Mentor will turbo-charge your personal, professional or business growth. But unless you have an incredible network, finding great Mentors has always been a challenge.</p>
    <p>GuideBridge Hub changes all that, levelling the playing field and making it easy for entrepreneurs and professionals to find the advice and guidance they deserve.</p>
    <p>No longer will you have to go searching for your perfect Mentor. We bring the perfect Mentor to you, selected from a global pool of experts, putting the power back in your hands and letting you get on with your growth.</p>
    <span class="btn-line">LET'S GET STARTED</span>
    <small>Register Free. 100% confidential. Obligation free.</small>
  </section>

  <section class="band d-mentor">
    <h2>Mentorship: But Different</h2>
    <div class="sub">Finding a Mentor used to be hard, but not any more.<br>We've turned the traditional model on its head, so now Mentors seek you.</div>
    <div class="d-cards">
      <div class="card blue">
        <svg class="ico" viewBox="0 0 38 38"><circle cx="19" cy="15" r="4" fill="#fff"/><circle cx="11" cy="17" r="3" fill="#fff"/><circle cx="27" cy="17" r="3" fill="#fff"/><path d="M12 28a7 7 0 0114 0z" fill="#fff"/><path d="M5 28a6 5 0 0110-3v3zM33 28a6 5 0 00-10-3v3z" fill="#fff"/></svg>
        <h3>Tell Us What You Need</h3>
        <p>There is no one size fits all approach to Mentorship. So tell us the challenges you are facing and the skill set your Mentor must have.</p>
      </div>
      <div class="card green">
        <svg class="ico" viewBox="0 0 38 38"><path d="M13 9h9l5 5v15H13z" fill="#fff"/><path d="M16 17h8M16 20h8M16 23h6" stroke="#34a21f" stroke-width="1.3"/></svg>
        <h3>Choose Your Mentor</h3>
        <p>Mentors are invited to Mentor you. We select 3 top picks that align with your criteria. It's then up to you whether you choose a Mentor, interview 1 or more or refine your criteria.</p>
      </div>
      <div class="card blue">
        <svg class="ico" viewBox="0 0 38 38"><path d="M9 19l20-9-5 19-5-6z" fill="#fff"/><path d="M19 23l10-13" stroke="#2b7fcb" stroke-width="1.2"/></svg>
        <h3>Ongoing Support</h3>
        <p>We don't step once you have your perfect Mentor. We're on hand to make life easy so you keep your sessions on track and provide ongoing support.</p>
      </div>
    </div>
    <span class="btn-line">REGISTER FOR FREE</span>
    <small>100% confidential and 100% obligation free.</small>
  </section>

  <section class="band d-how">
    <h2>HOW A MENTOR WILL<br><b>ACCELERATE YOUR GROWTH</b></h2>
    <div class="d-feats">
      <div class="feat">
        <div class="feat-title"><svg width="26" height="26" viewBox="0 0 26 26"><circle cx="13" cy="13" r="12" fill="none" stroke="#2b7fcb" stroke-width="1.5"/><path d="M7 9h12v7h-7l-3 3v-3H7z" fill="none" stroke="#2b7fcb" stroke-width="1.3"/></svg><span>Impartial<br>Advice</span></div>
        <p>Imagine being able to speak to someone who has been through the challenges you are currently facing? Who has "been there seen that" and can help you navigate the ups and downs of your career or business?</p>
      </div>
      <div class="feat">
        <div class="feat-title"><svg width="26" height="26" viewBox="0 0 26 26"><circle cx="13" cy="13" r="12" fill="none" stroke="#2b7fcb" stroke-width="1.5"/><path d="M13 6l7 13H6z" fill="none" stroke="#2b7fcb" stroke-width="1.3"/><path d="M13 11v4M13 16.5v1" stroke="#2b7fcb" stroke-width="1.3"/></svg><span>Avoid<br>the Pitfalls</span></div>
        <p>An experienced Mentor will help you see the challenges before they arise and make sure you avoid them altogether. Saving valuable time and money in the process.</p>
      </div>
      <div class="feat">
        <div class="feat-title"><svg width="26" height="26" viewBox="0 0 26 26"><circle cx="13" cy="13" r="12" fill="none" stroke="#2b7fcb" stroke-width="1.5"/><path d="M7 16v-3a6 6 0 0112 0v3" fill="none" stroke="#2b7fcb" stroke-width="1.3"/><rect x="6" y="14" width="3" height="5" fill="#2b7fcb"/><rect x="17" y="14" width="3" height="5" fill="#2b7fcb"/></svg><span>A Supportive<br>Ear</span></div>
        <p>Running a business and the challenges of corporate life can be extremely stressful. And often, our friends and family just don't get it. So imagine having someone independent who can understand where your coming from and.</p>
      </div>
      <div class="feat">
        <div class="feat-title"><svg width="26" height="26" viewBox="0 0 26 26"><circle cx="13" cy="13" r="12" fill="none" stroke="#2b7fcb" stroke-width="1.5"/><circle cx="13" cy="13" r="6" fill="none" stroke="#2b7fcb" stroke-width="1.3"/><circle cx="13" cy="13" r="2.5" fill="#2b7fcb"/></svg><span>Clarity</span></div>
        <p>Sometimes we are so caught up in our own world we struggle to see the big picture. Your Mentor will provide an objective, outsider view. Helping you to cut through the noise and focus on what's really important.</p>
      </div>
      <div class="feat">
        <div class="feat-title"><svg width="26" height="26" viewBox="0 0 26 26"><circle cx="13" cy="13" r="12" fill="none" stroke="#2b7fcb" stroke-width="1.5"/><path d="M8 18l3-3M11 15l7-8-1 6-4 4z" fill="none" stroke="#2b7fcb" stroke-width="1.3"/></svg><span>Motivation</span></div>
        <p>Your Mentor has seen this before and been in your shoes. They understand what your going through and will help you to re-focus and re-energize.</p>
      </div>
      <div class="feat">
        <div class="feat-title"><svg width="26" height="26" viewBox="0 0 26 26"><circle cx="13" cy="13" r="12" fill="none" stroke="#2b7fcb" stroke-width="1.5"/><rect x="8.5" y="7" width="9" height="12" fill="none" stroke="#2b7fcb" stroke-width="1.3"/><path d="M10.5 11h5M10.5 14h5" stroke="#2b7fcb" stroke-width="1.1"/></svg><span>Make You<br>Accountable</span></div>
        <p>A Mentor is not just there to pick you up - they are to give honest appraisal and tell you when your falling short. Ultimately, only you can control your success and your Mentor will hold you accountable to make sure you are.</p>
      </div>
    </div>
    <span class="btn-line">REGISTER FOR FREE</span>
    <small>Your closer to your perfect mentor than you think. Register today to see how easy it can be.</small>
  </section>

  <section class="band d-faq">
    <div class="faq-bg" role="img" aria-label="Faint background photo of a workspace"></div>
    <div class="inner">
      <h2>Frequently Asked Questions</h2>
      <div class="list">
        <div class="faq-item">What is a Mentor?<span class="plus">+</span></div>
        <div class="faq-item">Is a Mentor right for me?<span class="plus">+</span></div>
        <div class="faq-item">How often do we meet?<span class="plus">+</span></div>
        <div class="faq-open">How often you meet your Mentor is entirely up to you and something you should discuss and agree with your Mentor. Typically, we see that a Mentorship meeting every 2-4 weeks works well.</div>
        <div class="faq-item">Can I have more than one Mentor?<span class="plus">+</span></div>
        <div class="faq-item">What if it doesn't work out?<span class="plus">+</span></div>
        <div class="faq-item">How do we meet?<span class="plus">+</span></div>
        <div class="faq-item">What are the costs?<span class="plus">+</span></div>
      </div>
    </div>
  </section>

  <section class="band d-cta">
    <div class="cta-bg" role="img" aria-label="Green background with a faint connected network pattern"></div>
    <div class="inner">
      <h2>IT'S TIME TO INVEST IN YOU</h2>
      <p>If you've come this far you've already taken the most important step: recognising how mentorship can help you and taking action to find it. And now your here, the rest is easy.</p>
      <div class="hl">Get started now and let GuideBridge Hub do the rest...</div>
      <span class="btn-light">LET'S DO THIS</span>
      <small>Sign up is free, obligation free and 100% confidential</small>
    </div>
  </section>

  <footer class="band d-foot">
    <div class="links">Sitemap &nbsp;|&nbsp; Privacy Policy &nbsp;|&nbsp; Cookie Policy &nbsp;|&nbsp; Terms and Conditions</div>
    <div class="copy">GuideBridge Hub © 2018 All Rights Reserved.</div>
    <div class="socials"><span class="social"></span><span class="social"></span><span class="social" style="background:#d9453a"></span></div>
    <span class="top">⌃</span>
  </footer>
</main>

<!-- ===================== MOBILE ===================== -->
<main class="screen mobile">
  <header class="band m-nav">
    <span class="logo">GUIDEBRIDGE HUB</span>
    <span class="burger"></span>
  </header>

  <section class="band m-hero">
    <div class="hero-photo" role="img" aria-label="Photo of a mentor and two entrepreneurs in conversation at a bright office desk"></div>
    <div class="hero-shade"></div>
    <div class="inner">
      <div class="t1">GUIDEBRIDGE HUB</div>
      <div class="t2">A MENTOR FOR EVERYONE</div>
      <span class="btn-solid">FIND MY MENTOR</span>
    </div>
  </section>

  <section class="band m-find">
    <h2>FINDING A MENTOR HAS<br>NEVER BEEN EASIER</h2>
    <p>Having a great Mentor will turbo-charge your personal, professional or business growth. But unless you have an incredible network, finding great Mentors has always been a challenge.</p>
    <p>GuideBridge Hub changes all that, levelling the playing field and making it easy for entrepreneurs and professionals to find the advice and guidance they deserve.</p>
    <p>No longer will you have to go searching for your perfect Mentor. We bring the perfect Mentor to you, selected from a global pool of experts, putting the power back in your hands and letting you get on with your growth.</p>
    <span class="btn-line">LET'S GET STARTED</span>
    <small>Register Free. 100% confidential. Obligation free.</small>
  </section>

  <section class="band m-mentor">
    <h2>Mentorship: But<br>Different</h2>
    <div class="sub">Finding a Mentor used to be hard, but not any more. We've turned the traditional model on its head, so now Mentors seek you.</div>
    <div class="m-cards">
      <div class="card blue">
        <svg class="ico" viewBox="0 0 38 38"><circle cx="19" cy="15" r="4" fill="#fff"/><circle cx="11" cy="17" r="3" fill="#fff"/><circle cx="27" cy="17" r="3" fill="#fff"/><path d="M12 28a7 7 0 0114 0z" fill="#fff"/><path d="M5 28a6 5 0 0110-3v3zM33 28a6 5 0 00-10-3v3z" fill="#fff"/></svg>
        <h3>Tell Us What You Need</h3>
        <p>There is no one size fits all approach to Mentorship. So tell us the challenges you are facing and the skill set your Mentor must have.</p>
      </div>
      <div class="card green">
        <svg class="ico" viewBox="0 0 38 38"><path d="M13 9h9l5 5v15H13z" fill="#fff"/><path d="M16 17h8M16 20h8M16 23h6" stroke="#34a21f" stroke-width="1.3"/></svg>
        <h3>Choose Your Mentor</h3>
        <p>Mentors are invited to Mentor you. We select 3 top picks that align with your criteria. It's then up to you whether you choose a Mentor, interview 1 or more or refine your criteria.</p>
      </div>
      <div class="card blue">
        <svg class="ico" viewBox="0 0 38 38"><path d="M9 19l20-9-5 19-5-6z" fill="#fff"/><path d="M19 23l10-13" stroke="#2b7fcb" stroke-width="1.2"/></svg>
        <h3>Ongoing Support</h3>
        <p>We don't step once you have your perfect Mentor. We're on hand to make life easy so you keep your sessions on track and provide ongoing support.</p>
      </div>
    </div>
    <span class="btn-line">REGISTER FOR FREE</span>
    <small>100% confidential and 100% obligation free.</small>
  </section>

  <section class="band m-how">
    <h2>HOW A MENTOR<br>WILL <b>ACCELERATE<br>YOUR GROWTH</b></h2>
    <div class="m-feats">
      <div class="feat">
        <div class="feat-title"><svg width="16" height="16" viewBox="0 0 26 26"><circle cx="13" cy="13" r="12" fill="none" stroke="#2b7fcb" stroke-width="1.8"/><path d="M7 9h12v7h-7l-3 3v-3H7z" fill="none" stroke="#2b7fcb" stroke-width="1.5"/></svg><span>Impartial<br>Advice</span></div>
        <p>Imagine being able to speak to someone who has been through the challenges you are currently facing? Who has "been there seen that" and can help you navigate the ups and downs of your career or business?</p>
      </div>
      <div class="feat">
        <div class="feat-title"><svg width="16" height="16" viewBox="0 0 26 26"><circle cx="13" cy="13" r="12" fill="none" stroke="#2b7fcb" stroke-width="1.8"/><path d="M13 6l7 13H6z" fill="none" stroke="#2b7fcb" stroke-width="1.5"/></svg><span>Avoid<br>the Pitfalls</span></div>
        <p>An experienced Mentor will help you see the challenges before they arise and make sure you avoid them altogether. Saving valuable time and money in the process.</p>
      </div>
      <div class="feat">
        <div class="feat-title"><svg width="16" height="16" viewBox="0 0 26 26"><circle cx="13" cy="13" r="12" fill="none" stroke="#2b7fcb" stroke-width="1.8"/><path d="M7 16v-3a6 6 0 0112 0v3" fill="none" stroke="#2b7fcb" stroke-width="1.5"/><rect x="6" y="14" width="3" height="5" fill="#2b7fcb"/><rect x="17" y="14" width="3" height="5" fill="#2b7fcb"/></svg><span>A Supportive<br>Ear</span></div>
        <p>Running a business and the challenges of corporate life can be extremely stressful. And often, our friends and family just don't get it. So imagine having someone independent who can understand where your coming from and.</p>
      </div>
      <div class="feat">
        <div class="feat-title"><svg width="16" height="16" viewBox="0 0 26 26"><circle cx="13" cy="13" r="12" fill="none" stroke="#2b7fcb" stroke-width="1.8"/><circle cx="13" cy="13" r="6" fill="none" stroke="#2b7fcb" stroke-width="1.5"/><circle cx="13" cy="13" r="2.5" fill="#2b7fcb"/></svg><span>Clarity</span></div>
        <p>Sometimes we are so caught up in our own world we struggle to see the big picture. Your Mentor will provide an objective, outsider view. Helping you to cut through the noise and focus on what's really important.</p>
      </div>
      <div class="feat">
        <div class="feat-title"><svg width="16" height="16" viewBox="0 0 26 26"><circle cx="13" cy="13" r="12" fill="none" stroke="#2b7fcb" stroke-width="1.8"/><path d="M8 18l3-3M11 15l7-8-1 6-4 4z" fill="none" stroke="#2b7fcb" stroke-width="1.5"/></svg><span>Motivation</span></div>
        <p>Your Mentor has seen this before and been in your shoes. They understand what your going through and will help you to re-focus and re-energize.</p>
      </div>
      <div class="feat">
        <div class="feat-title"><svg width="16" height="16" viewBox="0 0 26 26"><circle cx="13" cy="13" r="12" fill="none" stroke="#2b7fcb" stroke-width="1.8"/><rect x="8.5" y="7" width="9" height="12" fill="none" stroke="#2b7fcb" stroke-width="1.5"/></svg><span>Make You<br>Accountable</span></div>
        <p>A Mentor is not just there to pick you up - they are to give honest appraisal and tell you when your falling short. Ultimately, only you can control your success and your Mentor will hold you accountable to make sure you are.</p>
      </div>
    </div>
    <span class="btn-line">REGISTER FOR FREE</span>
    <small>Your closer to your perfect mentor than you think. Register today to see how easy it can be.</small>
  </section>

  <section class="band m-faq">
    <div class="faq-bg" role="img" aria-label="Faint background photo of a workspace"></div>
    <div class="inner">
      <h2>Frequently<br>Asked Questions</h2>
      <div class="faq-item">What is a Mentor?<span class="plus">+</span></div>
      <div class="faq-item">Is a Mentor right for me?<span class="plus">+</span></div>
      <div class="faq-item">How often do we meet?<span class="plus">+</span></div>
      <div class="faq-open">How often you meet your Mentor is entirely up to you and something you should discuss and agree with your Mentor. Typically, we see that a Mentorship meeting every 2-4 weeks works well.</div>
      <div class="faq-item">Can I have more than one Mentor?<span class="plus">+</span></div>
      <div class="faq-item">What if it doesn't work out?<span class="plus">+</span></div>
      <div class="faq-item">How do we meet?<span class="plus">+</span></div>
      <div class="faq-item">What are the costs?<span class="plus">+</span></div>
    </div>
  </section>

  <section class="band m-cta">
    <div class="cta-bg" role="img" aria-label="Green background with a faint connected network pattern"></div>
    <div class="inner">
      <h2>IT'S TIME TO<br>INVEST IN YOU</h2>
      <p>If you've come this far you've already taken the most important step: recognising how mentorship can help you and taking action to find it. And now your here, the rest is easy.</p>
      <div class="hl">Get started now and let GuideBridge Hub do the rest...</div>
      <span class="btn-light">LET'S DO THIS</span>
      <small>Sign up is free, obligation free and 100% confidential</small>
    </div>
  </section>

  <footer class="band m-foot">
    <div class="links">Sitemap<br>Privacy Policy<br>Cookie Policy<br>Terms and Conditions</div>
    <div class="copy">GuideBridge Hub © 2018 All Rights Reserved.</div>
    <div class="socials"><span class="social"></span><span class="social"></span><span class="social" style="background:#d9453a"></span><span class="top">⌃</span></div>
  </footer>
</main>

</body>
</html>
```